Brochure Design Crest Harbour Advisory

Create a brochure, which sells my business. Utilise the website www.crestharbouradvisory.example for the details that need to go into the brochure. I would like 2 designs, one for a 4 page brochure and the other for a two page brochure (focus firstly on the 4 page).

The focus points are our 4 year rent guarantee and also out pitch that we are invested with them. Please see the website.

Need to focus on the main points as per the website, can use text from the website and the graphics where suitable.

On the 4 page brochure, first 3 pages to be info as per the website. On the 4 page of the brochure I would like the information included on the final 2 pages of the attached document (the investment property example). Please shrink this down, you do not need to include all the wording more so the figures.

The colours of the brochure to be blue, white and black

Target Market(s)

Property Investors

Industry/Entity Type

Business

Colors
0355a3
ffffff

Requirements
Must have
• Must have the main info on the website, (4 year rent guarantee) 'We are invested with you'
Nice to have
• Professional look

```html
<!DOCTYPE html>
<html lang="en">
<head>
<meta charset="utf-8">
<title>Crest Harbour Advisory – Brochure Spread</title>
<link rel="stylesheet" href="https://fonts.googleapis.com/css2?family=Oswald:wght@600;700&family=Arimo:wght@400;700&family=Carlito&display=swap">
<style>
  :root {
    --brand-blue: #0355a3;
    --deep-blue: #0a4596;
    --mid-blue: #1e6fc8;
    --sky-blue: #2aa3da;
    --heading-navy: #123a8c;
    --paper: #ffffff;
    --paper-tint: #e9ebf7;
    --ink: #1b1b1b;
    --ink-soft: #3a3a3a;
    --label-blue: #2b5fb8;
  }
  * { box-sizing: border-box; margin: 0; padding: 0; }
  html, body { width: 1200px; height: 1018px; overflow: hidden; background: #d9dbe0; }
  .spread { position: relative; width: 1200px; height: 1018px; display: flex; }
  .page {
    position: relative; width: 600px; height: 1018px; overflow: hidden;
    background: linear-gradient(160deg, var(--paper) 30%, var(--paper-tint) 100%);
    font-family: "Arimo", Arial, sans-serif; color: var(--ink);
  }
  .page + .page { border-left: 1px solid #c9ccd8; }
  .page-shapes { position: absolute; inset: 0; width: 100%; height: 100%; }

  .brand { position: absolute; top: 52px; left: 24px; display: flex; align-items: center; gap: 10px; }
  .brand-square { width: 34px; height: 34px; border: 3px solid var(--paper); }
  .brand-name { font-family: "Arimo", Arial, sans-serif; font-weight: 700; font-size: 15px; color: var(--paper); line-height: 1.1; width: 110px; }

  .page-title {
    position: absolute; font-family: "Oswald", "Arial Narrow", sans-serif; font-weight: 700;
    color: var(--heading-navy); letter-spacing: 0.3px; line-height: 1; white-space: nowrap;
  }
  .service-title { top: 66px; left: 318px; font-size: 28px; }
  .invest-title { top: 56px; left: 330px; font-size: 31px; }

  .photo {
    position: absolute; width: 116px; height: 72px; border: 3px solid var(--paper);
    box-shadow: 0 3px 8px rgba(0,0,0,0.25);
    background: linear-gradient(135deg, #dfe6f2, #8fb3dc);
  }
  .photo.dark { background: linear-gradient(135deg, #6d7a8c, #2a4f82); }
  .photo.blue { background: linear-gradient(135deg, #3d8ede, #0f62b8); }
  .photo.warm { background: linear-gradient(135deg, #e9e3da, #9a6b45); }

  .copy { position: absolute; font-size: 6.4px; line-height: 1.45; color: var(--ink-soft); }
  .copy .step { margin-bottom: 10px; }
  .copy .kicker { color: var(--label-blue); font-size: 6.4px; }
  .copy .step-title { font-weight: 700; color: var(--ink); margin-bottom: 4px; }

  .cycle { position: absolute; top: 14px; left: 484px; width: 112px; height: 130px; }
  .cycle text { font-family: "Arimo", Arial, sans-serif; }

  .security-title { top: 510px; left: 160px; width: 200px; text-align: center; font-size: 32px; }
  .security-sub { position: absolute; top: 556px; left: 100px; font-size: 22px; color: var(--brand-blue); font-family: "Arimo", Arial, sans-serif; }
  .security-copy { position: absolute; top: 592px; left: 100px; width: 300px; font-size: 9.4px; line-height: 1.3; color: var(--ink); }
  .security-copy p + p { margin-top: 10px; }
  .padlock {
    position: absolute; top: 560px; left: 432px; width: 90px; height: 150px; border-radius: 14px;
    background: linear-gradient(160deg, #c9d3df 0%, #7f9bbf 45%, #1f63b8 100%);
    box-shadow: 0 3px 8px rgba(0,0,0,0.2);
  }

  .contact-title { top: 742px; left: 62px; font-size: 21px; }
  .contact-lines { position: absolute; top: 780px; left: 16px; font-family: "Carlito", Calibri, sans-serif; font-size: 15px; line-height: 1.32; color: var(--heading-navy); font-style: normal; }
</style>
</head>
<body>
<main class="spread">

  <section class="page page-service">
    <svg class="page-shapes" viewBox="0 0 600 1018" preserveAspectRatio="none" aria-hidden="true">
      <path d="M0 0 H600 V18 C430 18 190 80 0 390 Z" fill="var(--mid-blue)"/>
      <path d="M0 0 H600 V10 C420 8 160 60 0 330 Z" fill="var(--deep-blue)"/>
      <path d="M0 1018 V958 C190 990 420 960 600 900 V1018 Z" fill="var(--brand-blue)"/>
      <path d="M0 952 C200 982 420 950 600 888 V898 C420 962 200 994 0 966 Z" fill="#ffffff"/>
    </svg>

    <div class="brand"><span class="brand-square"></span><span class="brand-name">Crest Harbour Advisory</span></div>

    <h1 class="page-title service-title">360 SERVICE</h1>

    <svg class="cycle" viewBox="0 0 110 130" role="img" aria-label="Seven step 360 degree service cycle">
      <g fill="var(--sky-blue)" stroke="#ffffff" stroke-width="1.5">
        <circle cx="58" cy="20" r="15"/><circle cx="92" cy="42" r="15"/><circle cx="96" cy="82" r="15"/>
        <circle cx="74" cy="114" r="15"/><circle cx="36" cy="112" r="15"/><circle cx="16" cy="80" r="15"/><circle cx="22" cy="42" r="15"/>
      </g>
      <circle cx="56" cy="70" r="24" fill="#0b0b0b"/>
      <text x="56" y="68" font-size="9" fill="#ffffff" text-anchor="middle">360°</text>
      <text x="56" y="79" font-size="8" fill="#ffffff" text-anchor="middle">Service</text>
      <g font-size="7" fill="#ffffff" text-anchor="middle" font-weight="700">
        <text x="58" y="15">1</text><text x="92" y="37">2</text><text x="96" y="77">3</text>
        <text x="74" y="109">4</text><text x="36" y="107">5</text><text x="16" y="75">6</text><text x="22" y="37">7</text>
      </g>
      <g font-size="3" fill="#ffffff" text-anchor="middle">
        <text x="58" y="25">Finance Check</text><text x="92" y="47">Set Goals</text><text x="96" y="87">Plan Strategy</text>
        <text x="74" y="119">Hot Spots</text><text x="36" y="117">Find Property</text><text x="16" y="85">Purchase</text><text x="22" y="47">Rent Out</text>
      </g>
    </svg>

    <div class="photo" style="top:118px; left:150px;" role="img" aria-label="Tablet showing a blue bar chart"></div>
    <div class="photo" style="top:245px; left:150px;" role="img" aria-label="Advisers reviewing finance documents at a desk"></div>
    <div class="photo dark" style="top:362px; left:150px;" role="img" aria-label="Tablet showing a goals presentation"></div>
    <div class="photo blue" style="top:472px; left:170px; width:72px; height:96px;" role="img" aria-label="Tablet showing a growth strategy page"></div>
    <div class="photo" style="top:598px; left:150px;" role="img" aria-label="Tablet showing a 3D house floor plan"></div>
    <div class="photo warm" style="top:716px; left:150px;" role="img" aria-label="Signing a property contract with a pen"></div>
    <div class="photo" style="top:842px; left:150px;" role="img" aria-label="Tablet showing a rental management dashboard"></div>

    <div class="copy" style="top:118px; left:312px; width:238px;">
      <div class="step"><div class="kicker">Identify Your Capacity</div><div class="step-title">Assess Finance Capacity</div>
        <p>The first step in your journey is to identify your finance capacity, with one of our investment broker specialists or your own trusted broker. This is a vital start point to determine what your portfolio potential is before progressing to establishing property goals.</p></div>
      <div class="step"><div class="kicker">What You Want</div><div class="step-title">Establish Property Goals</div>
        <p>The second step is to identify where you are trying to get to. While most want to reach wealth and retire early, every situation is different. We gather the information we need to identify your requirements and property types.</p></div>
      <div class="step"><div class="kicker">What Is Your Strategy</div><div class="step-title">Evaluate Property Strategy</div>
        <p>After establishing your capacity and property goals we can determine what your strategy should be to reach your goals. Should your property lean toward cash flow or capital growth? How many properties will you require?</p></div>
      <div class="step"><div class="kicker">Where To Buy</div><div class="step-title">Identify Market Hot Spots</div>
        <p>Now that we have established your strategy, our consultants get to work on finding hot spots. Using market research and statistical data we identify areas with strong growth indicators and stick to key locations in and around capital cities.</p></div>
      <div class="step"><div class="kicker">New House or Apartment</div><div class="step-title">Find Suitable Property</div>
        <p>Now that we have identified the market needs and ideal location we look to secure a suitable property that ticks all the boxes. We compare house and land packages as well as apartment options. Sit back and relax knowing you have the added security of the CHA 4 year rent guarantee.</p></div>
      <div class="step"><div class="kicker">Seal The Deal</div><div class="step-title">Purchase</div>
        <p>After choosing your property we will be there to deliver you the contracts and assist you with the purchase process. We recommend good solicitors and conveyancers and make sure the process is fluent and stress free.</p></div>
      <div class="step" style="margin-top:22px;"><div class="kicker">Secure Rent</div><div class="step-title">Rent And Manage</div>
        <p>The final stage is to have your property rented out and managed. If you are proceeding with our 4 year rent guarantee you will be renting through our partnered property manager with low fees. Once you are cash flow positive we head back to the start of our 360 degree cycle to keep your portfolio moving forward.</p></div>
    </div>
  </section>

  <section class="page page-invest">
    <svg class="page-shapes" viewBox="0 0 600 1018" preserveAspectRatio="none" aria-hidden="true">
      <path d="M0 0 H600 V16 C420 16 170 70 0 330 Z" fill="var(--mid-blue)"/>
      <path d="M0 0 H600 V8 C410 6 150 50 0 280 Z" fill="var(--deep-blue)"/>
      <path d="M0 1018 V1000 C200 1010 420 990 600 950 V1018 Z" fill="var(--brand-blue)"/>
      <path d="M0 994 C200 1004 420 980 600 938 V948 C420 992 200 1012 0 1006 Z" fill="#ffffff"/>
    </svg>

    <div class="brand"><span class="brand-square"></span><span class="brand-name">Crest Harbour Advisory</span></div>

    <h1 class="page-title invest-title">INVEST WITH US</h1>

    <div class="photo" style="top:150px; left:150px;" role="img" aria-label="Tablet showing a rising red bar chart"></div>
    <div class="photo" style="top:282px; left:150px;" role="img" aria-label="Hands reviewing financial charts on paper"></div>
    <div class="photo blue" style="top:405px; left:150px;" role="img" aria-label="Tablet showing a negative gearing page"></div>

    <div class="copy" style="top:140px; left:385px; width:195px;">
      <div class="step"><div class="kicker">Create Wealth</div><div class="step-title">Capital Growth</div>
        <p>First and foremost, capital growth is the driving force behind property investing and the primary reason property is such a loved investment option for Australians. Over the last hundred years one fact about property remains evident: in the long term property increases in value.</p></div>
      <div class="step"><div class="kicker">Instant Cash</div><div class="step-title">Cash Flow</div>
        <p>Whilst capital growth is important, many investors have little spare cash and don't want to be dipping into their own pockets to maintain their portfolio. With strong knowledge of the current market it is possible to achieve cash flow positive investments that also have strong growth factors.</p></div>
      <div class="step"><div class="kicker">Powerful Tool</div><div class="step-title">Negative Gearing</div>
        <p>With the government attempting to increase investors in the market to assist with undersupply, certain tax incentives may be applied to property investments, the main one being the ability to negative gear a property. Negative gearing can turn a property that is making a loss into a gain by offsetting the loss against your income.</p></div>
    </div>

    <h2 class="page-title security-title">SECURITY</h2>
    <div class="security-sub">4 Year Rent Guarantee</div>
    <div class="security-copy">
      <p>We provide a 4 year rent guarantee on selected properties. One week after the completion of your new property CHA will pay you an agreed market rent for 4 straight years. No need to worry about finding tenants or collecting rent, we have that covered.</p>
      <p>CHA will take on the task of sourcing tenants and collecting rent on your behalf. Any short falls in rent or vacancy periods will be at CHA expense. Meaning for the first 4 years we are taking on the rental risk, hence the phrase 'We are invested with you'! Contact CHA for further details on the terms and conditions of this offer.</p>
    </div>
    <div class="padlock" role="img" aria-label="Blue and silver combination padlock"></div>

    <h2 class="page-title contact-title">CONTACT US</h2>
    <address class="contact-lines">
      Address: Level 3, Harbourview House<br>
      12 Example Lane,<br>
      Northgate NSW 2999 Australia<br>
      Phone: 1300 555 014<br>
      Email: admin@crestharbouradvisory.example
    </address>
  </section>

</main>
</body>
</html>
```